Potential SF Gazette Best Seller Poetry Book Cover Contest

I’m penning my first poetry book. It’s entitled “Lanterns Under Rain”
I’m fairly open to creative freedom but I want the cover to without a doubt catch a persons' eye instantly because first impressions are VERY IMPORTANT in the literary world
I tend to lean towards a luxury look and colors like black, gold, rose gold, silver, glitter etc but again I’m open to interpretation
Looking forward to your submissions
Target Market(s)
those seeking relatable love advice and quotes
modern millenials
Colors
Look and feel

```html
<!DOCTYPE html>
<html lang="en">
<head>
<meta charset="utf-8">
<title>Lanterns Under Rain — Cover</title>
<link rel="stylesheet" href="https://fonts.googleapis.com/css2?family=Montserrat:wght@800&display=swap">
<style>
  :root {
    --paper: #ffffff;
    --frame: #1a1a1a;
    --gold-light: #e9b545;
    --gold-mid: #dba23a;
    --gold-deep: #c4831f;
    --ink: #000000;
  }
  html, body {
    margin: 0;
    padding: 0;
    width: 1200px;
    height: 1200px;
    overflow: hidden;
    background: var(--paper);
  }
  .cover {
    position: absolute;
    left: 290px;
    top: 168px;
    width: 595px;
    height: 875px;
    border: 1px solid var(--frame);
    background: var(--paper);
    box-sizing: border-box;
    overflow: hidden;
  }
  .cover-title {
    position: absolute;
    left: -2px;
    top: 318px;
    margin: 0;
    font-family: "Montserrat", sans-serif;
    font-weight: 800;
    font-size: 112px;
    line-height: 128px;
    letter-spacing: -0.035em;
    text-transform: lowercase;
  }
  .title-line {
    display: block;
    white-space: nowrap;
  }
  .title-line--gold {
    background: linear-gradient(100deg, var(--gold-deep) 0%, var(--gold-mid) 40%, var(--gold-light) 100%);
    -webkit-background-clip: text;
    background-clip: text;
    color: transparent;
  }
  .title-line--ink {
    color: var(--ink);
  }
</style>
</head>
<body>
  <main class="cover">
    <h1 class="cover-title">
      <span class="title-line title-line--gold">lanterns</span>
      <span class="title-line title-line--gold">under</span>
      <span class="title-line title-line--ink">rain.</span>
    </h1>
  </main>
</body>
</html>
```